Lifestyle brand needs lip balm label design

We need a label design for lip balm tubes. The name of our company is "quorvalent"

Design Description:
Our lip balm tubes will be black. The label itself will be clear/transparent. We would like to create a gradient effect with the color green (same shade as our logo) starting from the bottom and slowly fading out to clear so that the black tube is visible (example of gradient shown in attached image)

We have two lip balm flavors: mint and lemongrass.
We would like the top/clear portion of the label to say "MINT" (all caps) . The second label should say "LEMONGRASS" (all caps) in the same location. Our logo "quorvalent" should be in the bottom/green portion of the label. Below the logo, we would like the words "NATURAL BALM" (all caps) in white text

```html
<!DOCTYPE html>
<html lang="en">
<head>
<meta charset="utf-8">
<title>Quorvalent Natural Balm Labels</title>
<link rel="stylesheet" href="https://fonts.googleapis.com/css2?family=Cabin:wght@500&family=Jost:wght@400&display=swap">
<style>
  :root {
    --tube-black: #000000;
    --leaf-green: #7a924b;
    --label-white: #ffffff;
    --page-bg: #ffffff;
  }
  html, body {
    margin: 0;
    padding: 0;
    width: 1200px;
    height: 1154px;
    overflow: hidden;
    background: var(--page-bg);
  }
  .label-sheet {
    display: block;
    width: 1200px;
    height: 1154px;
  }
  .flavor-name {
    font-family: "Cabin", "Gill Sans", sans-serif;
    font-weight: 500;
    font-size: 72px;
    fill: var(--leaf-green);
  }
  .product-type {
    font-family: "Cabin", "Gill Sans", sans-serif;
    font-weight: 500;
    font-size: 25px;
    letter-spacing: 10.5px;
    fill: var(--label-white);
  }
  .brand-name {
    font-family: "Jost", "Futura", sans-serif;
    font-weight: 400;
    font-size: 76px;
    letter-spacing: 1px;
    fill: var(--tube-black);
  }
</style>
</head>
<body>
<svg class="label-sheet" viewBox="0 0 1200 1154" xmlns="http://www.w3.org/2000/svg" aria-label="Quorvalent natural balm labels: Mint and Lemongrass">
  <defs>
    <linearGradient id="tube-fade" x1="0" y1="0" x2="0" y2="1">
      <stop offset="0" stop-color="#000000"/>
      <stop offset="0.265" stop-color="#000000"/>
      <stop offset="0.31" stop-color="#0d0f09"/>
      <stop offset="0.40" stop-color="#1f2415"/>
      <stop offset="0.50" stop-color="#353f21"/>
      <stop offset="0.60" stop-color="#4d5e30"/>
      <stop offset="0.69" stop-color="#637b3c"/>
      <stop offset="0.765" stop-color="#7a924b"/>
      <stop offset="1" stop-color="#7a924b"/>
    </linearGradient>
  </defs>

  <g class="label label-mint">
    <rect class="label-body" x="0" y="0" width="583" height="1154" fill="url(#tube-fade)"/>
    <text class="flavor-name" x="291" y="200" text-anchor="middle">MINT</text>
    <text class="product-type" x="296" y="237" text-anchor="middle">NATURAL BALM</text>
    <text class="brand-name" x="291" y="1007" text-anchor="middle">quorvalent</text>
  </g>

  <g class="label label-lemongrass">
    <rect class="label-body" x="618" y="0" width="582" height="1154" fill="url(#tube-fade)"/>
    <text class="flavor-name" x="908" y="200" text-anchor="middle">LEMONGRASS</text>
    <text class="product-type" x="913" y="237" text-anchor="middle">NATURAL BALM</text>
    <text class="brand-name" x="909" y="1007" text-anchor="middle">quorvalent</text>
  </g>
</svg>
</body>
</html>
```